IT Services Business Card Design

We require a business card design for an IT services company called RT Code Transit.

We specialize in taking an organisations software and readying it for deployment to new environments (e.g. Nex 3 to Nex 5). This process is termed application packaging. This is not the same as putting things in boxes but I am happy to use boxes as a pun icon ;-) This is our second step in branding, we currently have a new logo and our poor excuse of a website is next to be updated but it contains information on who we are and what we cover at rtcodetransit.example

We are looking for a fun, modern but stylish and professional looking design.

I have attached the logo in multiple formats including vector formats (and the fonts that created the logo if required)
Updates

Thanks to all the designers so far, some great designs in there.  I will be selecting a card design on the deadline date. 

However, there is still time to submit some more designs.  The majority of the ones I have so far are typical simplistic designs that we have all seen before and I have enough of those to choose from now.  If you wish to submit any more designs, please submit somthing unusual to grab our attention.

Target Market(s)

Project executives of large organisations looking for Nexora migrations

Industry/Entity Type

Software

Requirements
Must have
• Want to show company name, contact name, title, main number, contact number, fax number, email address and website address. I do not want to show the address.
Must use the attached logo, retaining the colours in them.

This has to be a double-sided design. I will be using pelby.example and will be selecting their rounded corner business card design.

Their templates and design requirements (sizing etc.) can be found here: http://uk.pelby.example/help/faq/templates-and-guidelines.html

Happy for company name or website to be on either side of the card.

This design has to be original and not used before for another company

Would like to style it around the business colours in the logo
Nice to have
• Pelby.example has an option for multiple card designs to appear on the back. If this is possible in the budget and time you have and you have a design(s) that work with that but carry the same style and theme, that would be nice to see but not necessary.
Should not have
• We do not want to put a postal address on the cards

```html
<!DOCTYPE html>
<html lang="en">
<head>
<meta charset="utf-8">
<title>RT Code Transit – Business Card</title>
<link rel="stylesheet" href="https://fonts.googleapis.com/css2?family=Arimo:wght@400;700&display=swap">
<style>
  :root {
    --page-bg: #ededee;
    --card-white: #ffffff;
    --card-black: #0b0b0c;
    --ink-dark: #4a4744;
    --ink-mid: #5e5b58;
    --rule: #8f8c89;
    --accent-blue: #8796d4;
    --mark-light: #d9d9d9;
  }
  * { box-sizing: border-box; margin: 0; padding: 0; }
  html, body {
    width: 1200px; height: 864px; overflow: hidden;
    background: var(--page-bg);
    font-family: "Arimo", Arial, sans-serif;
  }
  .canvas {
    position: relative; width: 1200px; height: 864px;
    display: flex; align-items: center; justify-content: center; gap: 40px;
  }
  .card {
    position: relative; width: 540px; height: 350px;
    border-radius: 28px; overflow: hidden;
    box-shadow: 0 6px 18px rgba(0,0,0,0.18);
  }
  .card--back {
    background: radial-gradient(circle at 80% 20%, #2a2a2c 0%, var(--card-black) 60%);
  }
  .card--front { background: var(--card-white); }

  .brand-mark {
    position: absolute; display: flex; align-items: center; gap: 12px;
    font-weight: 400; letter-spacing: 0.5px; white-space: nowrap;
  }
  .brand-mark__dot {
    width: 30px; height: 30px; border-radius: 50%;
    background: var(--accent-blue); flex: none;
  }
  .card--back .brand-mark {
    left: 46px; bottom: 56px; font-size: 34px; color: var(--mark-light);
  }
  .card--front .brand-mark {
    left: 36px; top: 70px; font-size: 30px; color: var(--ink-dark);
  }

  .contact-person {
    position: absolute; right: 30px; top: 110px; text-align: right;
  }
  .contact-person__name { font-size: 19px; font-weight: 700; color: var(--ink-mid); line-height: 1; }
  .contact-person__title { font-size: 10px; font-weight: 700; color: var(--ink-mid); margin-top: 4px; }

  .divider {
    position: absolute; left: 36px; right: 30px; top: 150px;
    height: 1px; background: var(--rule);
  }

  .contact-list {
    position: absolute; right: 30px; top: 164px; list-style: none;
    font-size: 13px; color: var(--ink-mid); line-height: 22px;
  }
  .contact-list li {
    display: flex; justify-content: flex-end; align-items: center; gap: 8px;
  }
  .contact-list .icon { width: 16px; height: 14px; flex: none; }
</style>
</head>
<body>
<main class="canvas">
  <section class="card card--back" aria-label="Card back">
    <div class="brand-mark"><span class="brand-mark__dot"></span>RT Code Transit</div>
  </section>

  <section class="card card--front" aria-label="Card front">
    <div class="brand-mark"><span class="brand-mark__dot"></span>RT Code Transit</div>

    <div class="contact-person">
      <p class="contact-person__name">Dana Lorrimer</p>
      <p class="contact-person__title">President</p>
    </div>

    <div class="divider"></div>

    <ul class="contact-list">
      <li>0800 555 0142
        <svg class="icon" viewBox="0 0 16 14" aria-label="Phone"><rect width="16" height="14" rx="2" fill="var(--accent-blue)"/><path d="M5 3.5c-.8.6-.8 2 .5 3.8 1.3 1.7 2.9 2.9 4 3 .6 0 1.1-.5 1.3-1l-1.6-1.2-.9.6C7.6 8.3 6.6 7.2 6.2 6.3l.7-.8L6 3.5z" fill="#fff"/></svg>
      </li>
      <li>0800 555 0198
        <svg class="icon" viewBox="0 0 16 14" aria-label="Fax"><rect width="16" height="14" rx="2" fill="var(--accent-blue)"/><rect x="4" y="3" width="8" height="3" fill="#fff"/><rect x="3" y="6.5" width="10" height="4.5" rx="1" fill="#fff"/></svg>
      </li>
      <li>Enquiries@RTCodeTransit.example
        <svg class="icon" viewBox="0 0 16 14" aria-label="Email"><rect width="16" height="14" rx="2" fill="var(--accent-blue)"/><rect x="3" y="4" width="10" height="6.5" fill="#fff"/><path d="M3 4l5 3.5L13 4" stroke="var(--accent-blue)" fill="none"/></svg>
      </li>
      <li>www.RTCodeTransit.example
        <svg class="icon" viewBox="0 0 16 14" aria-label="Website"><rect width="16" height="14" rx="2" fill="var(--accent-blue)"/><circle cx="8" cy="7" r="4" fill="none" stroke="#fff"/><path d="M4 7h8M8 3v8" stroke="#fff"/></svg>
      </li>
    </ul>
  </section>
</main>
</body>
</html>
```